New Business Card Design*

We are a recruitment company based in Norwich/Cambridge England.
I have included our company logo which we want to remain the same.

What we are looking for is a new creative Business card which will really stand out!!

Contact Information for Business Card

Harriet Dunmore
email: Harriet@vexalim.co.uk
Address: Larkwell House
Brambleton Enterprise Quarter
Thistlebrook Road
Norwich
QX9 2LB
Tel:01632 418305

```html
<!DOCTYPE html>
<html lang="en">
<head>
<meta charset="utf-8">
<title>Vexalim Business Card</title>
<link rel="stylesheet" href="https://fonts.googleapis.com/css2?family=Poppins:wght@400;500;600&display=swap">
<style>
  :root {
    --backdrop: #1d1d20;
    --card-grey: #8e8b91;
    --card-grey-soft: #99969c;
    --card-white: #ffffff;
    --ink-grey: #75737a;
    --ink-light: #8a888f;
    --brand-green: #7cc242;
    --faint: #efeff0;
  }
  * { box-sizing: border-box; margin: 0; padding: 0; }
  html, body { width: 1200px; height: 864px; overflow: hidden; }
  body {
    background: var(--backdrop);
    font-family: "Poppins", sans-serif;
    position: relative;
  }
  .card {
    position: absolute;
    top: 282px;
    width: 520px;
    height: 300px;
    border-radius: 18px;
    overflow: hidden;
  }
  /* Back of card */
  .card-back { left: 40px; background: var(--card-grey); }
  .card-back .decor-circle {
    position: absolute; right: -30px; top: -40px;
    width: 260px; height: 260px; border-radius: 50%;
    background: var(--card-grey-soft);
  }
  .card-back .brand {
    position: absolute; left: 140px; top: 112px;
    display: flex; align-items: center; gap: 14px;
  }
  .brand-dot { border-radius: 50%; flex: none; }
  .card-back .brand-dot { width: 46px; height: 46px; background: var(--card-white); }
  .brand-name { font-weight: 600; line-height: 1; letter-spacing: -0.5px; }
  .card-back .brand-name { font-size: 48px; color: var(--card-white); }
  .brand-tagline {
    font-size: 8px; letter-spacing: 3.2px; text-transform: uppercase;
    margin-top: 4px; font-weight: 500;
  }
  .card-back .brand-tagline { color: var(--card-white); }
  .card-back .web {
    position: absolute; left: 240px; top: 214px;
    font-size: 14px; color: var(--card-white); letter-spacing: 0.5px;
  }

  /* Front of card */
  .card-front { left: 640px; background: var(--card-white); }
  .card-front .decor-circle {
    position: absolute; right: 10px; top: -30px;
    width: 190px; height: 190px; border-radius: 50%;
    background: var(--faint);
  }
  .card-front .brand {
    position: absolute; left: 34px; top: 92px;
    display: flex; align-items: center; gap: 12px;
  }
  .card-front .brand-dot { width: 36px; height: 36px; background: var(--brand-green); }
  .card-front .brand-name { font-size: 40px; color: var(--ink-grey); }
  .card-front .brand-tagline { color: var(--ink-grey); font-size: 7px; }
  .person { position: absolute; left: 34px; top: 160px; }
  .person-name { font-size: 24px; font-weight: 600; color: var(--ink-grey); line-height: 1.1; }
  .person-name .surname { color: var(--brand-green); }
  .person-title { font-size: 13px; color: var(--ink-grey); margin-top: 2px; }
  .divider { position: absolute; left: 34px; top: 214px; width: 170px; height: 1px; background: #b9b8bc; }
  .contacts { position: absolute; left: 34px; top: 222px; list-style: none; }
  .contacts li {
    display: flex; align-items: center; gap: 8px;
    font-size: 11.5px; color: var(--ink-grey); line-height: 18px;
  }
  .contacts svg { width: 13px; height: 13px; flex: none; }
  .address-rule { position: absolute; left: 250px; top: 128px; width: 240px; height: 1px; background: #b9b8bc; }
  .address {
    position: absolute; right: 30px; top: 138px;
    text-align: right; font-size: 12px; line-height: 17px; color: var(--ink-light);
  }
  .edge-band { position: absolute; left: 0; top: 0; width: 520px; height: 300px; }
</style>
</head>
<body>
  <section class="card card-back" aria-label="Card back">
    <div class="decor-circle"></div>
    <div class="brand">
      <span class="brand-dot"></span>
      <div>
        <div class="brand-name">Vexalim</div>
        <div class="brand-tagline">Technology Recruitment</div>
      </div>
    </div>
    <div class="web">www.vexalim.co.uk</div>
  </section>

  <section class="card card-front" aria-label="Card front">
    <div class="decor-circle"></div>
    <div class="brand">
      <span class="brand-dot"></span>
      <div>
        <div class="brand-name">Vexalim</div>
        <div class="brand-tagline">Technology Recruitment</div>
      </div>
    </div>

    <div class="person">
      <div class="person-name">Harriet <span class="surname">Dunmore</span></div>
      <div class="person-title">Managing Director</div>
    </div>
    <div class="divider"></div>
    <ul class="contacts">
      <li>
        <svg viewBox="0 0 14 14"><circle cx="7" cy="7" r="7" fill="#7cc242"/><path d="M4.6 3.8c.4-.3.8-.2 1 .2l.6 1.1c.2.3.1.6-.2.8l-.4.3c.3.8.9 1.4 1.7 1.8l.3-.4c.2-.3.5-.4.8-.2l1.1.6c.4.2.5.6.2 1l-.4.5c-.4.4-1 .5-1.6.2-1.7-.8-2.9-2-3.6-3.6-.3-.6-.2-1.2.2-1.6z" fill="#fff"/></svg>
        0163-2418-305
      </li>
      <li>
        <svg viewBox="0 0 14 14"><circle cx="7" cy="7" r="7" fill="#7cc242"/><rect x="3.5" y="4.5" width="7" height="5" rx=".6" fill="#fff"/><path d="M3.8 4.9 7 7.3l3.2-2.4" stroke="#7cc242" stroke-width=".8" fill="none"/></svg>
        Harriet@vexalim.co.uk
      </li>
      <li>
        <svg viewBox="0 0 14 14"><circle cx="7" cy="7" r="7" fill="#7cc242"/><circle cx="7" cy="7" r="3.6" stroke="#fff" stroke-width=".8" fill="none"/><ellipse cx="7" cy="7" rx="1.5" ry="3.6" stroke="#fff" stroke-width=".8" fill="none"/><path d="M3.4 7h7.2" stroke="#fff" stroke-width=".8"/></svg>
        www.vexalim.co.uk
      </li>
    </ul>

    <div class="address-rule"></div>
    <address class="address" style="font-style:normal">
      Larkwell House<br>
      Brambleton Enterprise Quarter<br>
      Thistlebrook Road, Norwich, QX9 2LB
    </address>

    <svg class="edge-band" viewBox="0 0 520 300" aria-hidden="true">
      <path d="M0 300 L0 293 L360 293 C372 293 374 258 388 258 L520 258 L520 300 Z" fill="#8e8b91"/>
      <path d="M30 288 L356 288 C368 288 370 253 384 253" stroke="#7cc242" stroke-width="3" fill="none"/>
    </svg>
  </section>
</body>
</html>
```